Design our branded business card!

We'd love for you to design our business card and come up with a fitting design that reflects the Pivex brand. We're a growing tech startup with big ambitions. We've included our brand guidelines (contain colour palette), logo (EPS vector in CMYK) and old designs to help you on your way.

We'd like to keep the design fairly simple:

* Name
* Phone number
* Email address
* Website (www.pivex.life)
* Twitter (@pivex)
* Address (18 Wexham Row, Leeds, UK, LS9 4ZQ).

This would need to include print and cutting marks.

If you have any questions just let us know!

Target Market(s)

Businesses, Press and our customers!

Industry/Entity Type

Business

Contact Information for Business Card

* Name
* Phone number
* Email address
* Twitter (@pivex)

Font styles to use
Sans Serif

Requirements
Must have
• 1. Must have the Pivex logo included.
• 2. Must use the font 'Brandon Text' in either 'light' or 'thin' (https://www.typevault-demo.com/fonts/qrsfonts/halden-sans/)
• 3. Must use exact colours references from the brand guidelines. Colours outside of the brand guidelines will be discounted. White (transparent) backgrounds are fine.
• 4. Must contain the following information:
• * Name
• * Phone number
• * Email address
• * Website (www.pivex.life)
• * Twitter (@pivex)
• * Address (18 Wexham Row, Leeds, UK, LS9 4ZQ).
Nice to have
• Must use the font 'Brandon Text' in either 'light' or 'thin' (https://www.typevault-demo.com/fonts/qrsfonts/halden-sans/)
Should not have
• Colours outside of the brand guidelines will be discounted. White (transparent) backgrounds are fine.
• Avoid creating icons or including photography.

```html
<!DOCTYPE html>
<html lang="en">
<head>
<meta charset="utf-8">
<title>Pivex business card</title>
<link href="https://fonts.googleapis.com/css2?family=Open+Sans:wght@300;400;700&display=swap" rel="stylesheet">
<style>
  :root {
    --backdrop: #2a2a2a;
    --card: #f7f8f7;
    --brand-green: #7bbd6f;
    --brand-green-faint: #e9f3e6;
    --ink: #2e3a37;
    --ink-name: #1e3a2e;
  }
  html, body {
    margin: 0;
    width: 1200px;
    height: 834px;
    overflow: hidden;
    background: var(--backdrop);
    font-family: "Open Sans", Arial, sans-serif;
  }
  .canvas {
    position: relative;
    width: 1200px;
    height: 834px;
    display: flex;
    flex-direction: column;
    align-items: center;
    justify-content: center;
    gap: 40px;
  }
  .card {
    position: relative;
    width: 600px;
    height: 343px;
    background: var(--card);
    overflow: hidden;
  }
  .wordmark {
    display: flex;
    align-items: center;
    gap: 14px;
  }
  .wordmark__dot {
    border-radius: 50%;
    background: var(--brand-green);
    flex: none;
  }
  .wordmark__name {
    font-weight: 300;
    color: var(--ink);
    line-height: 1;
  }
  .card--front .wordmark {
    position: absolute;
    left: 50%;
    top: 50%;
    transform: translate(-50%, -50%);
  }
  .card--front .wordmark__dot { width: 70px; height: 70px; }
  .card--front .wordmark__name { font-size: 72px; letter-spacing: 1px; }

  .card--back .backdrop-circle {
    position: absolute;
    left: 60px;
    top: -40px;
    width: 300px;
    height: 300px;
    border-radius: 50%;
    background: var(--brand-green-faint);
  }
  .card--back .wordmark {
    position: absolute;
    left: 36px;
    bottom: 40px;
    gap: 10px;
  }
  .card--back .wordmark__dot { width: 48px; height: 48px; }
  .card--back .wordmark__name { font-size: 50px; }

  .contact {
    position: absolute;
    left: 385px;
    top: 58px;
    color: var(--ink);
    font-size: 11.5px;
  }
  .contact__name {
    margin: 0;
    font-weight: 700;
    font-size: 15px;
    color: var(--ink-name);
  }
  .contact__role {
    margin: 2px 0 12px;
    font-size: 12px;
    color: var(--brand-green);
  }
  .contact__address { margin: 0 0 8px; }
  .contact__list {
    list-style: none;
    margin: 0;
    padding: 0;
  }
  .contact__item {
    display: flex;
    align-items: center;
    gap: 10px;
    height: 20px;
  }
  .contact__icon {
    width: 12px;
    height: 12px;
    flex: none;
    color: var(--brand-green);
  }
</style>
</head>
<body>
<main class="canvas">
  <section class="card card--front" aria-label="Card front">
    <div class="wordmark">
      <span class="wordmark__dot"></span>
      <span class="wordmark__name">pivex</span>
    </div>
  </section>

  <section class="card card--back" aria-label="Card back">
    <div class="backdrop-circle"></div>
    <div class="wordmark">
      <span class="wordmark__dot"></span>
      <span class="wordmark__name">pivex</span>
    </div>
    <div class="contact">
      <p class="contact__name">Martin Hale</p>
      <p class="contact__role">President</p>
      <p class="contact__address">18 Wexham Row, Leeds, UK, LS9 4ZQ</p>
      <ul class="contact__list">
        <li class="contact__item">
          <svg class="contact__icon" viewBox="0 0 12 12" aria-hidden="true"><path d="M1 4 Q6 0 11 4 L9 5 L8 4 Q6 3 4 4 L3 5 Z M3 6 H9 V10 H3 Z" fill="none" stroke="currentColor" stroke-width="1"/></svg>
          <span>+44 (0) 7700 900 318</span>
        </li>
        <li class="contact__item">
          <svg class="contact__icon" viewBox="0 0 12 12" aria-hidden="true"><rect x="1" y="2.5" width="10" height="7" fill="none" stroke="currentColor" stroke-width="1"/><path d="M1 2.5 L6 7 L11 2.5" fill="none" stroke="currentColor" stroke-width="1"/></svg>
          <span>martin@pivex.life</span>
        </li>
        <li class="contact__item">
          <svg class="contact__icon" viewBox="0 0 12 12" aria-hidden="true"><circle cx="6" cy="6" r="4.5" fill="currentColor"/></svg>
          <span>@pivex</span>
        </li>
        <li class="contact__item">
          <svg class="contact__icon" viewBox="0 0 12 12" aria-hidden="true"><circle cx="6" cy="6" r="5" fill="none" stroke="currentColor" stroke-width="1"/><ellipse cx="6" cy="6" rx="2.2" ry="5" fill="none" stroke="currentColor" stroke-width="1"/><path d="M1 6 H11" stroke="currentColor" stroke-width="1"/></svg>
          <span>www.pivex.life</span>
        </li>
      </ul>
    </div>
  </section>
</main>
</body>
</html>
```